Data Analytics Platform Website Design

Website design for a new data analytics platform called Metrica Core. I need a design that is simple but informative, professional but still sexy and that is aimed at the business professional instead of being "technical". I have a logo (picture uploaded) and also screenshots from the platform itself and I can also provide example websites from competitors that are similar in design and layout to what I need. I also have the messaging but I need help with photos, icons, font, layout, etc. I want to utilize some of the colors in the logo, but I want the overall color scheme to utilize darker blues (more serious feeling, less playful) with one accent color for highlighting. This design cannot be "fun", "playful", or "cheerful" and should instead be "professional", "serious", but still uncluttered and clean cut. However, simple does not mean easy because I want to see transitions that are clean and high level. I want the final design to be all of that while showing the company and our product as capable, serious, and reliable.

Example websites:
1. www.valdrenix.com
2. q7.ai
3. corvelane.com
4. https://www.pym.com/en_us/software/lorsa.html
5. https://www.belvoro.com/
6. gwendel.ai

Target Market(s)

Business Professionals - Government/large companies/data analytics focused

Industry/Entity Type

Data Science

Number of Pages Required

3 page

Font styles to use
Serif
Sans Serif

Requirements
Must have
• It must be clean and professional. Cannot be cluttered or too "busy". No playful or childish looks at all.
Nice to have
• I want to see professional designs but also professional concepts incorporated.
Should not have
• Should not have Comic Sans or the like, no playful or "techy" themes

```html
<!DOCTYPE html>
<html lang="en">
<head>
<meta charset="utf-8">
<title>Metrica Core — Data Analytics Platform</title>
<link href="https://fonts.googleapis.com/css2?family=Poppins:wght@400;500;600;700&family=Lato:wght@400;700&display=swap" rel="stylesheet">
<style>
  :root {
    --navy: #0f2a6b;
    --ink: #1b1b1b;
    --text: #3a3a3a;
    --rule: #16128a;
    --accent: #3f3fe0;
    --accent-2: #2f6df0;
    --blob: #e4e5f4;
    --band: #f1f1f8;
    --footer-a: #3a4ce8;
    --footer-b: #1ea6f6;
    --footer-bar: #0e1c3c;
    --white: #ffffff;
    --nav: #555a66;
  }
  * { box-sizing: border-box; margin: 0; padding: 0; }
  html, body { width: 1200px; height: 2343px; overflow: hidden; }
  body { position: relative; background: var(--white); font-family: "Lato", sans-serif; color: var(--text); }

  .blob { position: absolute; border-radius: 50%; background: var(--blob); }
  .band { position: absolute; left: 0; top: 505px; width: 1200px; height: 135px; background: var(--band); box-shadow: 0 3px 4px rgba(0,0,0,.08); }

  .site-header { position: absolute; left: 0; top: 0; width: 1200px; height: 82px; background: var(--white); box-shadow: 0 2px 6px rgba(0,0,0,.08); z-index: 3; }
  .brand { position: absolute; left: 144px; top: 22px; display: flex; align-items: center; gap: 10px; font-family: "Poppins", sans-serif; font-size: 25px; letter-spacing: 1px; color: #2a2f3a; }
  .brand-mark { width: 30px; height: 26px; background: var(--accent-2); }
  .main-nav { position: absolute; left: 584px; top: 31px; font-family: "Poppins", sans-serif; font-size: 13px; color: var(--nav); }
  .main-nav span { position: absolute; white-space: nowrap; }
  .btn-start { position: absolute; left: 945px; top: 28px; width: 111px; height: 22px; background: var(--accent); color: var(--white); font-family: "Poppins", sans-serif; font-size: 12px; font-weight: 500; text-align: center; line-height: 22px; border-radius: 2px; }

  .hero-kicker { position: absolute; left: 145px; top: 256px; font-family: "Poppins", sans-serif; font-size: 20px; letter-spacing: 3px; color: var(--ink); }
  .hero-title { position: absolute; left: 144px; top: 278px; font-family: "Poppins", sans-serif; font-weight: 700; font-size: 56px; color: var(--navy); letter-spacing: -.5px; white-space: nowrap; }
  .hero-sub { position: absolute; left: 144px; top: 346px; font-family: "Poppins", sans-serif; font-size: 25px; color: var(--ink); white-space: nowrap; }
  .btn { position: absolute; width: 128px; height: 37px; background: linear-gradient(90deg, #3b3fe0, #2f78f2); color: var(--white); font-family: "Lato", sans-serif; font-weight: 700; font-size: 13px; text-align: center; line-height: 37px; border-radius: 2px; }
  .hero-art { position: absolute; left: 692px; top: 140px; width: 436px; height: 322px; background: linear-gradient(135deg, #eef0fb, #d7dcf5 55%, #f4d6e0); border-radius: 4px; }
  .slide-arrow { position: absolute; width: 32px; height: 32px; border-radius: 50%; background: #4a4a4a; }

  .feature { position: absolute; top: 565px; width: 294px; height: 150px; background: var(--white); border-top: 10px solid var(--rule); box-shadow: 0 3px 10px rgba(0,0,0,.12); }
  .feature.is-active { background: linear-gradient(120deg, #4a3fe0, #1aa3f3); color: var(--white); }
  .feature svg.icon { position: absolute; left: 16px; top: 20px; }
  .feature h3 { position: absolute; left: 81px; top: 20px; font-family: "Lato", sans-serif; font-weight: 400; font-size: 18px; color: #222; }
  .feature p { position: absolute; left: 81px; top: 51px; width: 205px; font-size: 12.5px; line-height: 19px; color: #444; }
  .feature.is-active h3, .feature.is-active p { color: var(--white); }
  .feature svg.go { position: absolute; right: 16px; bottom: 13px; }

  .photo { position: absolute; }
  .eyebrow { position: absolute; font-family: "Lato", sans-serif; font-size: 19px; color: #333; }
  .section-title { position: absolute; font-family: "Lato", sans-serif; font-weight: 700; font-size: 40px; line-height: 57px; color: #333; white-space: nowrap; }
  .title-rule { position: absolute; width: 141px; height: 3px; background: var(--rule); }
  .body-copy { position: absolute; width: 430px; font-size: 14.3px; line-height: 22.4px; color: #444; }

  .laptop-screen { position: absolute; left: 596px; top: 1167px; width: 512px; height: 347px; background: linear-gradient(180deg, #2a2d34, #1c1e24); border-radius: 14px 14px 0 0; border: 10px solid #15161a; border-bottom: 0; }
  .laptop-base { position: absolute; left: 537px; top: 1512px; width: 630px; height: 16px; background: linear-gradient(180deg, #e3e4e8, #a8aab0); border-radius: 2px 2px 10px 10px; }

  .site-footer { position: absolute; left: 0; top: 2022px; width: 1200px; height: 273px; background: linear-gradient(90deg, var(--footer-a), var(--footer-b)); color: var(--white); }
  .footer-brand { position: absolute; left: 144px; top: 104px; display: flex; align-items: center; gap: 10px; font-family: "Poppins", sans-serif; font-size: 31px; letter-spacing: 1px; }
  .footer-brand .brand-mark { width: 38px; height: 32px; background: var(--white); }
  .social { position: absolute; top: 161px; width: 33px; height: 33px; border-radius: 50%; border: 1.5px solid var(--white); }
  .footer-col { position: absolute; top: 36px; }
  .footer-col h4 { font-family: "Lato", sans-serif; font-weight: 700; font-size: 15.5px; margin-bottom: 6px; }
  .footer-col li { list-style: none; font-size: 12.5px; line-height: 20px; padding-left: 4px; }
  .footer-bar { position: absolute; left: 0; top: 2295px; width: 1200px; height: 48px; background: var(--footer-bar); color: var(--white); text-align: center; font-size: 13.5px; line-height: 48px; }
</style>
</head>
<body>

  <div class="blob" style="left:-37px;top:-55px;width:256px;height:256px;"></div>
  <div class="blob" style="left:1115px;top:20px;width:140px;height:140px;"></div>
  <div class="band"></div>
  <div class="blob" style="left:-50px;top:500px;width:260px;height:260px;"></div>
  <div class="blob" style="left:1060px;top:550px;width:260px;height:260px;"></div>
  <div class="blob" style="left:-80px;top:680px;width:560px;height:560px;"></div>
  <div class="blob" style="left:920px;top:1100px;width:620px;height:520px;"></div>
  <div class="blob" style="left:-60px;top:1860px;width:500px;height:400px;"></div>

  <header class="site-header">
    <div class="brand"><span class="brand-mark"></span>Metrica Core</div>
    <nav class="main-nav">
      <span style="left:0">Platform</span>
      <span style="left:82px">Solutions</span>
      <span style="left:168px">Initiatives</span>
      <span style="left:257px">Customers</span>
    </nav>
    <div class="btn-start">GET STARTED</div>
  </header>

  <section class="hero">
    <div class="slide-arrow" style="left:71px;top:343px;">
      <svg width="32" height="32" viewBox="0 0 32 32"><path d="M18 10l-6 6 6 6" fill="none" stroke="#fff" stroke-width="2"/></svg>
    </div>
    <div class="hero-kicker">Welcome to</div>
    <h1 class="hero-title">Metrica Core</h1>
    <p class="hero-sub">Neque porro quisquam est qui dolorem</p>
    <div class="btn" style="left:146px;top:393px;">LEARN MORE</div>
    <div class="hero-art" role="img" aria-label="Illustration of analysts reviewing bar charts, a pie chart and dashboards"></div>
    <div class="slide-arrow" style="left:1097px;top:343px;">
      <svg width="32" height="32" viewBox="0 0 32 32"><path d="M14 10l6 6-6 6" fill="none" stroke="#fff" stroke-width="2"/></svg>
    </div>
  </section>

  <section class="features">
    <article class="feature is-active" style="left:144px;">
      <svg class="icon" width="52" height="46" viewBox="0 0 52 46" fill="none" stroke="#fff" stroke-width="2"><rect x="1" y="1" width="48" height="40"/><line x1="1" y1="9" x2="49" y2="9"/><circle cx="6" cy="5" r="1"/><circle cx="11" cy="5" r="1"/><path d="M36 36l4 4 8-9" stroke-width="2.5"/></svg>
      <h3>Lorem Ipsum</h3>
      <p>Lorem Ipsum has been the standard dummy text ever since the</p>
      <svg class="go" width="22" height="12" viewBox="0 0 22 12" fill="none" stroke="#fff" stroke-width="1.5"><path d="M0 6h20M15 1l5 5-5 5"/></svg>
    </article>
    <article class="feature" style="left:453px;">
      <svg class="icon" width="52" height="52" viewBox="0 0 52 52" fill="none" stroke="#111" stroke-width="2"><rect x="1" y="1" width="50" height="50"/><rect x="6" y="5" width="10" height="16"/><rect x="21" y="5" width="10" height="16"/><rect x="36" y="5" width="10" height="16"/><circle cx="11" cy="40" r="4"/><circle cx="26" cy="40" r="4"/><circle cx="41" cy="40" r="4"/><line x1="18" y1="1" x2="18" y2="51"/><line x1="34" y1="1" x2="34" y2="51"/></svg>
      <h3>Lorem Ipsum</h3>
      <p>Lorem Ipsum has been the standard dummy text ever since the</p>
      <svg class="go" width="22" height="12" viewBox="0 0 22 12" fill="none" stroke="#16128a" stroke-width="1.5"><path d="M0 6h20M15 1l5 5-5 5"/></svg>
    </article>
    <article class="feature" style="left:762px;">
      <svg class="icon" width="50" height="46" viewBox="0 0 50 46" fill="none" stroke="#111" stroke-width="2"><path d="M48 2L2 22l16 6 30-26-22 30 8 12 14-42z"/><path d="M18 28v14l8-10"/></svg>
      <h3>Lorem Ipsum</h3>
      <p>Lorem Ipsum has been the standard dummy text ever since the</p>
      <svg class="go" width="22" height="12" viewBox="0 0 22 12" fill="none" stroke="#16128a" stroke-width="1.5"><path d="M0 6h20M15 1l5 5-5 5"/></svg>
    </article>
  </section>

  <section class="about">
    <div class="photo" style="left:143px;top:784px;width:447px;height:342px;background:linear-gradient(135deg,#0d3a6e,#1a7fc0 50%,#5fc6ea);" role="img" aria-label="Photo of business people discussing data charts on a tablet"></div>
    <div class="eyebrow" style="left:632px;top:804px;">About</div>
    <h2 class="section-title" style="left:632px;top:821px;">Metrica Core</h2>
    <div class="title-rule" style="left:632px;top:885px;"></div>
    <p class="body-copy" style="left:632px;top:910px;">Lorem Ipsum is simply dummy text of the printing and typesetting industry. Lorem Ipsum has been the industry's standard dummy text ever since the 1500s, when an unknown printer took a galley of type and scrambled it to make a type specimen book. It has survived not only five centuries, but also the leap into electronic typesetting, remaining essentially unchanged.</p>
    <div class="btn" style="left:632px;top:1065px;">LEARN MORE</div>
  </section>

  <section class="product">
    <h2 class="section-title" style="left:144px;top:1185px;">Can you help translate<br>this site into</h2>
    <div class="title-rule" style="left:144px;top:1306px;"></div>
    <p class="body-copy" style="left:144px;top:1330px;">Lorem Ipsum is simply dummy text of the printing and typesetting industry. Lorem Ipsum has been the industry's standard dummy text ever since the 1500s, when an unknown printer took a galley of type and scrambled it to make a type specimen book. It has survived not only five centuries, but also the leap into electronic typesetting, remaining essentially unchanged.</p>
    <div class="btn" style="left:144px;top:1485px;">LEARN MORE</div>
    <div class="laptop-screen" role="img" aria-label="Laptop showing the platform's organization administration dashboard"></div>
    <div class="laptop-base" aria-hidden="true"></div>
  </section>

  <section class="passage">
    <div class="photo" style="left:143px;top:1592px;width:447px;height:341px;background:linear-gradient(160deg,#1b2a8a,#2250c0 45%,#e2473f 70%,#16307e);" role="img" aria-label="Isometric illustration of a glowing data cube with people working around it"></div>
    <div class="eyebrow" style="left:632px;top:1611px;">Finibus Bonorum</div>
    <h2 class="section-title" style="left:632px;top:1628px;">Lorem Ipsum passage</h2>
    <div class="title-rule" style="left:632px;top:1692px;"></div>
    <p class="body-copy" style="left:632px;top:1718px;">Lorem Ipsum is simply dummy text of the printing and typesetting industry. Lorem Ipsum has been the industry's standard dummy text ever since the 1500s, when an unknown printer took a galley of type and scrambled it to make a type specimen book. It has survived not only five centuries, but also the leap into electronic typesetting, remaining essentially unchanged.</p>
    <div class="btn" style="left:632px;top:1872px;">LEARN MORE</div>
  </section>

  <footer class="site-footer">
    <div class="footer-brand"><span class="brand-mark"></span>Metrica Core</div>
    <span class="social" style="left:194px;"></span>
    <span class="social" style="left:231px;"></span>
    <span class="social" style="left:268px;"></span>
    <span class="social" style="left:304px;"></span>
    <div class="footer-col" style="left:494px;">
      <h4>PLATFORM</h4>
      <ul><li>Overview</li><li>Pricing</li><li>Supported technologies</li><li>Application Performance</li><li>Infrastructure Monitoring</li><li>Cloud Automation</li><li>Application Security</li><li>Digital Experience</li><li>AIOps</li></ul>
    </div>
    <div class="footer-col" style="left:700px;">
      <h4>PLATFORM</h4>
      <ul><li>Overview</li><li>Cloud operations</li><li>Microservices &amp; container</li><li>DevOps</li><li>Observability</li><li>Cloud monitoring</li><li>Application monitoring</li><li>Vela Assistant</li></ul>
    </div>
    <div class="footer-col" style="left:928px;">
      <h4>ABOUT</h4>
      <ul><li>Overview</li><li>Leadership</li><li>Investor Relations</li><li>News</li><li>Media kit</li><li>Careers</li><li>Partners</li><li>Locations</li><li>Contact us</li></ul>
    </div>
  </footer>
  <div class="footer-bar">Metrica Core© 2021 All Rights Reserved | Privacy Policy | Terms and Conditions</div>

</body>
</html>
```